Business Card Design

Just looking for a good designs that looks good with our company logo. I'd like it to be simple and to the point. Just including contact information, our logo, and my name somewhere on the card so future clients know who they're contacting, and a couple services offered. The two images I attached are pictures of our logo. I don't care which color they they are, I just attached both images to give a reference of logo colors depending on the color of the card.
Names: Calvin Prewitt
Phone: 555-247-9061
Email: tidyturfcrew@mailvista.net
Services offered:
Mowing
Fertilization
Aeration
Bed & tree maintenance
and more.
Industry/Entity Type
Business
Contact Information for Business Card
Names: Calvin Prewitt
Phone: 555-247-9061
Look and feel

```html
<!DOCTYPE html>
<html lang="en">
<head>
<meta charset="UTF-8">
<title>Tidy Turf Crew – Business Card</title>
<link href="https://fonts.googleapis.com/css2?family=Lato:wght@400;700;900&display=swap" rel="stylesheet">
<style>
  :root {
    --backdrop: #2a2a2c;
    --card: #fbfbfa;
    --navy: #2d3042;
    --red: #e1503b;
    --white: #ffffff;
  }
  * { margin: 0; padding: 0; box-sizing: border-box; }
  html, body {
    width: 1200px;
    height: 900px;
    overflow: hidden;
    background: var(--backdrop);
    font-family: "Lato", sans-serif;
  }
  .card {
    position: absolute;
    left: 100px;
    top: 164px;
    width: 1000px;
    height: 572px;
    background: var(--card);
    box-shadow: 0 20px 50px rgba(0,0,0,0.45);
  }
  .brand {
    position: absolute;
    left: 0;
    top: 0;
    width: 430px;
    height: 572px;
    display: flex;
    align-items: center;
    justify-content: center;
    gap: 16px;
  }
  .brand-dot {
    width: 38px;
    height: 38px;
    border-radius: 50%;
    background: var(--red);
    flex: none;
  }
  .brand-name {
    font-weight: 900;
    font-size: 40px;
    color: var(--navy);
    letter-spacing: 0.5px;
  }
  .divider {
    position: absolute;
    left: 430px;
    top: 90px;
    width: 4px;
    height: 392px;
    background: linear-gradient(to bottom, rgba(225,80,59,0), var(--red) 55%);
  }
  .details {
    position: absolute;
    left: 482px;
    top: 112px;
    right: 40px;
  }
  .person-name {
    font-weight: 900;
    font-size: 34px;
    color: var(--navy);
    letter-spacing: 0.5px;
  }
  .person-title {
    font-weight: 700;
    font-size: 21px;
    color: var(--red);
    letter-spacing: 1px;
    margin-top: 2px;
  }
  .contact-list {
    list-style: none;
    margin-top: 36px;
  }
  .contact-item {
    display: flex;
    align-items: center;
    gap: 14px;
    font-weight: 700;
    font-size: 27px;
    color: var(--red);
    margin-bottom: 16px;
  }
  .contact-icon { width: 28px; height: 24px; flex: none; }
  .services-label {
    display: inline-block;
    margin-top: 40px;
    margin-left: 118px;
    padding: 8px 22px;
    background: var(--navy);
    color: var(--white);
    font-weight: 700;
    font-size: 24px;
    letter-spacing: 1px;
  }
  .services-list {
    margin-top: 14px;
    font-weight: 700;
    font-size: 26px;
    line-height: 1.28;
    color: var(--navy);
    text-align: right;
    padding-right: 6px;
  }
</style>
</head>
<body>
  <main class="card">
    <div class="brand">
      <span class="brand-dot"></span>
      <span class="brand-name">Tidy Turf Crew</span>
    </div>
    <div class="divider"></div>
    <section class="details">
      <h1 class="person-name">CALVIN PREWITT</h1>
      <p class="person-title">DESIGNATION</p>
      <ul class="contact-list">
        <li class="contact-item">
          <svg class="contact-icon" viewBox="0 0 28 24" aria-hidden="true">
            <path d="M2 9 Q14 0 26 9 L22 11 L19 7 Q14 5 9 7 L6 11 Z" fill="#e1503b"/>
            <rect x="5" y="12" width="18" height="10" rx="2" fill="#e1503b"/>
            <circle cx="14" cy="17" r="2.6" fill="#fbfbfa"/>
          </svg>
          <span>555-247-9061</span>
        </li>
        <li class="contact-item">
          <svg class="contact-icon" viewBox="0 0 28 24" aria-hidden="true">
            <rect x="2" y="4" width="24" height="16" fill="#e1503b"/>
            <path d="M2 4 L14 14 L26 4" fill="none" stroke="#fbfbfa" stroke-width="2"/>
          </svg>
          <span>tidyturfcrew@mailvista.net</span>
        </li>
      </ul>
      <div class="services-label">SERVICES OFFERED</div>
      <p class="services-list">Mowing / Fertilization / Aeration<br>Bed &amp; tree Maintenance &amp; more.</p>
    </section>
  </main>
</body>
</html>
```